Bakery Mix Package Design

We are looking for a fresh new package design that conveys a European flare but has a lot character and integrity and when you see it you think, this is a ‘Gourmet’ product line. This box design will be the 1s in a Series of mixes where we will slightly alter the picture and text to reflect the other product mixes. The design layout should be able to be used for multiple bakery mixes. I’m open when it come to color and I will trust your design judgment in terms of what looks good and appealing on a store shelf. The package should feature either Belgian Waffle or French Crepes somewhere in the middle as these are the 1st two product we are launching. This middle space should be able to accommodate cakes, chocolate mouse images as these are upcoming mixes in development. So that is why it’s key to have a design that can be reused multiple times.
The brand Name is "Maudrel's Kitchen" and should be visible and noticeable on the packaging. We do not have a logo for brand name so please come up with a mock up design of how that should appear.
Example of packages we like visit her for some ideas. http://www.bovalette.com/gamme-bovalette/les-essentiels-ma-pate-a-gaufres-_R_19_18_.htm

```html
<!DOCTYPE html>
<html lang="en">
<head>
<meta charset="utf-8">
<title>Maudrel's Kitchen – French Crepes Bakery Mix</title>
<link rel="stylesheet" href="https://fonts.googleapis.com/css2?family=Bungee&family=Yesteryear&display=swap">
<style>
  :root {
    --brand-red: #ee1c2e;
    --cream: #fdf1b3;
    --panel-cream: #fbf6de;
    --page: #ffffff;
    --frame-line: #d9d4c4;
    --photo-light: #f4efe8;
    --photo-warm: #e9cf9f;
  }
  * { margin: 0; padding: 0; box-sizing: border-box; }
  html, body {
    width: 891px;
    height: 1200px;
    overflow: hidden;
    background: var(--page);
  }
  .package {
    position: relative;
    width: 891px;
    height: 1200px;
    background: var(--panel-cream);
    border: 3px solid var(--frame-line);
    overflow: hidden;
  }
  .top-band {
    position: absolute;
    left: 0; top: 0;
    width: 100%;
    height: 298px;
    background: var(--brand-red);
  }
  .brand-name {
    position: absolute;
    left: 94px;
    top: 40px;
    font-family: "Bungee", sans-serif;
    font-weight: 400;
    font-size: 82px;
    line-height: 104px;
    color: var(--cream);
    letter-spacing: 1px;
    text-transform: uppercase;
  }
  .mix-badge {
    position: absolute;
    left: 556px;
    top: 210px;
    width: 296px;
    height: 110px;
    border-radius: 50%;
    background: var(--cream);
    display: flex;
    align-items: center;
    justify-content: center;
    font-family: "Yesteryear", cursive;
    font-size: 56px;
    color: var(--brand-red);
  }
  .product-title {
    position: absolute;
    left: 0;
    top: 392px;
    width: 100%;
    text-align: center;
    font-family: "Yesteryear", cursive;
    font-weight: 400;
    font-size: 104px;
    line-height: 132px;
    color: var(--brand-red);
  }
  .product-photo {
    position: absolute;
    left: 90px;
    top: 534px;
    width: 738px;
    height: 480px;
    border: 17px solid var(--brand-red);
    background: linear-gradient(180deg, var(--photo-light) 0%, var(--photo-warm) 100%);
  }
  .bottom-band {
    position: absolute;
    left: 0;
    bottom: 0;
    width: 100%;
    height: 108px;
    background: var(--brand-red);
  }
</style>
</head>
<body>
  <main class="package">
    <header class="top-band">
      <h1 class="brand-name">Maudrel's<br>Kitchen</h1>
    </header>
    <div class="mix-badge">Bakery Mix</div>
    <h2 class="product-title">French Crepes</h2>
    <div class="product-photo" role="img" aria-label="Product photo: a folded crepe with ice cream and berry sauce on a white plate"></div>
    <footer class="bottom-band"></footer>
  </main>
</body>
</html>
```